stationary for hygienic company

We need a stationary design for hygienic company which provides public high end sanitary products and high end public lavatory.
We need a fresh and clean style stationary
we want the following things:
* logo (redesigned in eps/vector)
* Letterhead (with company details)
* letterhead (without company details)
* Business card
* note block
* ballpoint
* etcetera (a complete package)

```html
<!DOCTYPE html>
<html lang="fr">
<head>
<meta charset="utf-8">
<title>Veloura – Business Card</title>
<link href="https://fonts.googleapis.com/css2?family=Didact+Gothic&family=Montserrat:wght@600&display=swap" rel="stylesheet">
<style>
  :root {
    --backdrop: #e9e7e3;
    --card: #ffffff;
    --ink: #3a3a3c;
    --muted: #8a8a8e;
    --pink: #e8399a;
    --blue: #3bb2e6;
  }
  * { box-sizing: border-box; margin: 0; padding: 0; }
  html, body {
    width: 1200px; height: 1184px; overflow: hidden;
    background: var(--backdrop);
    font-family: "Didact Gothic", "Helvetica Neue", Arial, sans-serif;
    color: var(--ink);
  }
  .sheet {
    width: 1200px; height: 1184px;
    display: flex; flex-direction: column; align-items: center; justify-content: center;
    gap: 40px;
  }
  .card {
    position: relative;
    width: 900px; height: 514px;
    background: linear-gradient(135deg, #ffffff 55%, #f1f1f2 100%);
    box-shadow: 0 10px 30px rgba(0,0,0,.12);
  }

  /* Brand block */
  .brand { display: flex; flex-direction: column; align-items: center; }
  .brand-name {
    display: flex; align-items: center; gap: 14px;
    font-size: 96px; line-height: 1; color: var(--ink); letter-spacing: 1px;
  }
  .brand-dot { width: 26px; height: 26px; border-radius: 50%; background: var(--pink); }
  .brand-tagline { font-size: 30px; margin-top: 6px; }
  .brand-note { font-size: 10px; color: var(--muted); margin-top: 4px; align-self: flex-start; }

  /* Front */
  .card-front .brand { position: absolute; left: 50%; top: 50%; transform: translate(-50%, -50%); }

  /* Back */
  .card-back .brand { position: absolute; left: 70px; top: 90px; align-items: flex-start; }
  .card-back .brand-name { font-size: 72px; }
  .card-back .brand-tagline { font-size: 24px; margin-left: 30px; }
  .card-back .brand-note { margin-left: 30px; }

  .holder { position: absolute; left: 500px; top: 80px; }
  .holder-name { font-family: "Montserrat", sans-serif; font-weight: 600; font-size: 26px; letter-spacing: .5px; }
  .holder-name .first { color: var(--pink); }
  .holder-name .last { color: var(--blue); }
  .holder-title { font-size: 12px; letter-spacing: 9px; color: var(--muted); margin-top: 4px; }
  .address { display: flex; align-items: center; gap: 12px; margin-top: 40px; font-size: 14px; color: var(--muted); }

  .contacts {
    position: absolute; left: 160px; bottom: 70px;
    display: grid; grid-template-columns: 230px 260px; row-gap: 18px;
    font-size: 15px; color: var(--muted);
  }
  .contact { display: flex; align-items: center; gap: 12px; }
  .icon { width: 18px; height: 18px; fill: var(--pink); flex: none; }
</style>
</head>
<body>
<main class="sheet">

  <section class="card card-front" aria-label="Card front">
    <div class="brand">
      <div class="brand-name"><span class="brand-dot"></span>Veloura</div>
      <div class="brand-tagline">Boutique Hygienique</div>
    </div>
  </section>

  <section class="card card-back" aria-label="Card back">
    <div class="brand">
      <div class="brand-name"><span class="brand-dot"></span>Veloura</div>
      <div class="brand-tagline">Boutique Hygienique</div>
      <div class="brand-note">Marque déposée</div>
    </div>

    <div class="holder">
      <div class="holder-name"><span class="first">NAME</span><span class="last">SURNAME</span></div>
      <div class="holder-title">TITLE</div>
      <div class="address">
        <svg class="icon" viewBox="0 0 24 24" aria-hidden="true"><path d="M12 2a7 7 0 0 0-7 7c0 5 7 13 7 13s7-8 7-13a7 7 0 0 0-7-7zm0 9.5A2.5 2.5 0 1 1 12 6.5a2.5 2.5 0 0 1 0 5z"/></svg>
        <span>123 et fath St, maleona, gbly, mazoreta</span>
      </div>
    </div>

    <div class="contacts">
      <div class="contact">
        <svg class="icon" viewBox="0 0 24 24" aria-hidden="true"><path d="M6.6 10.8a15 15 0 0 0 6.6 6.6l2.2-2.2a1 1 0 0 1 1-.25 11.4 11.4 0 0 0 3.6.57 1 1 0 0 1 1 1V20a1 1 0 0 1-1 1A17 17 0 0 1 3 4a1 1 0 0 1 1-1h3.5a1 1 0 0 1 1 1 11.4 11.4 0 0 0 .57 3.6 1 1 0 0 1-.25 1z"/></svg>
        <span>+2 123-456-789</span>
      </div>
      <div class="contact">
        <svg class="icon" viewBox="0 0 24 24" aria-hidden="true"><rect x="6" y="2" width="12" height="4" rx="1"/><rect x="3" y="7" width="18" height="11" rx="2"/><rect x="7" y="15" width="10" height="7"/></svg>
        <span>+2 123-456-789</span>
      </div>
      <div class="contact">
        <svg class="icon" viewBox="0 0 24 24" aria-hidden="true"><path d="M7 1h10a2 2 0 0 1 2 2v18a2 2 0 0 1-2 2H7a2 2 0 0 1-2-2V3a2 2 0 0 1 2-2zm0 3v14h10V4z"/></svg>
        <span>+2 123-456-789</span>
      </div>
      <div class="contact">
        <svg class="icon" viewBox="0 0 24 24" aria-hidden="true"><path d="M2 5h20v14H2zm2 2v.4l8 5 8-5V7z"/></svg>
        <span>name@website.com</span>
      </div>
    </div>
  </section>

</main>
</body>
</html>
```